Modern Banner for use on Emails and Electronic letters.

We need a Email banner that we can also uses as a banner on electronic documents . Would be a bonus to be able to use banner on pixmingle.
The banner should incorporate our logo and company name; The ProVela Group.
We would like an eye catching, modern design.
We are completely open to using colour and/or images along with our logo and company name.
Currently the font for our company name is time new roman but again we are open to suggestions. The company name can be be moved away from the umbrella logo to anywhere in the banner.

Industry/Entity Type

Electronic

Font styles to use
Serif
Sans Serif

Colors

Designer to choose colors to be used in the design.

Requirements
Must have
• ProVela Logo (Umbrella design - Black umbrella on red blocks with a letter on each block spelling VELA.
• Company name: The ProVela Group
• Be Modern and professional.
• Suitable for use as an email banner but can also be used as letterhead on electronic documents.
Nice to have
• Colour and/or images.
• Be able to be used as pixmingle banner.

```html
<!DOCTYPE html>
<html lang="en">
<head>
<meta charset="utf-8">
<title>The ProVela Group – Letterhead and Email Banner</title>
<link rel="stylesheet" href="https://fonts.googleapis.com/css2?family=Tinos:wght@400&display=swap">
<style>
  :root {
    --backdrop: #85868a;
    --paper: #ffffff;
    --ink: #000000;
    --accent-red: #c8372d;
    --text-light: #ffffff;
    --watermark: #ececec;
  }
  html, body {
    margin: 0;
    padding: 0;
    overflow: hidden;
  }
  .canvas {
    position: relative;
    width: 1200px;
    height: 1200px;
    background: var(--backdrop);
    overflow: hidden;
    font-family: "Tinos", "Times New Roman", serif;
  }
  .letterhead {
    position: absolute;
    left: 70px;
    top: 284px;
    width: 490px;
    height: 632px;
    background: var(--paper);
  }
  .email-banner {
    position: absolute;
    left: 620px;
    top: 520px;
    width: 520px;
    height: 160px;
    background: var(--paper);
  }
  svg { display: block; width: 100%; height: 100%; }
  .band { fill: var(--ink); }
  .slash { fill: var(--accent-red); }
  .company-name {
    fill: var(--text-light);
    font-family: "Tinos", "Times New Roman", serif;
  }
  .brand-mark {
    fill: var(--ink);
    font-family: "Tinos", "Times New Roman", serif;
  }
  .brand-square { fill: var(--accent-red); }
  .brand-watermark {
    fill: var(--watermark);
    font-family: "Tinos", "Times New Roman", serif;
  }
</style>
</head>
<body>
<main class="canvas">

  <section class="letterhead" aria-label="The ProVela Group letterhead">
    <svg viewBox="0 0 490 632" xmlns="http://www.w3.org/2000/svg">
      <g class="letterhead-header">
        <polygon class="band" points="0,25 42,25 22,101 0,101"/>
        <polygon class="slash" points="38,25 45,25 26,101 19,101"/>
        <rect class="brand-square" x="92" y="42" width="12" height="12"/>
        <text class="brand-mark" x="98" y="78" font-size="20" text-anchor="middle">ProVela</text>
        <polygon class="slash" points="177,25 184,25 167,101 160,101"/>
        <polygon class="band" points="186,25 490,25 490,101 168,101"/>
        <text class="company-name" x="193" y="73" font-size="31">The ProVela Group</text>
      </g>
      <text class="brand-watermark" x="245" y="345" font-size="60" text-anchor="middle">ProVela</text>
      <rect class="band" x="0" y="625" width="490" height="7"/>
    </svg>
  </section>

  <section class="email-banner" aria-label="The ProVela Group email banner">
    <svg viewBox="0 0 650 200" xmlns="http://www.w3.org/2000/svg">
      <polygon class="band" points="25,54 72,54 52,146 25,146"/>
      <polygon class="slash" points="68,54 76,54 56,146 48,146"/>
      <rect class="brand-square" x="141" y="70" width="14" height="14"/>
      <text class="brand-mark" x="148" y="116" font-size="25" text-anchor="middle">ProVela</text>
      <polygon class="slash" points="236,54 244,54 224,146 216,146"/>
      <polygon class="band" points="246,54 625,54 625,146 226,146"/>
      <text class="company-name" x="262" y="113" font-size="39">The ProVela Group</text>
    </svg>
  </section>

</main>
</body>
</html>
```